A.I. Software PowerPoint Presentation

We need a PowerPoint presentation design for our artificial intelligence product vxMender.

We've attached our current PowerPoint to use as a base. This presentation is used to introduce and describe what the product is, how it works, why you need it, what makes it better than other solutions, and how to implement it.

We would like the PowerPoint design to be more professional-looking as we present to executives and CIOs of banks, government, and other large corporations. We are a tech startup and would like the design to convey the feel of innovation and high-tech, but also trustworthy, reputable, and capable, for the more conservative audiences.

The PowerPoint should have minimal use of animation (animate only if necessary). It should be modern and clean and not too busy.

We appreciate design work on all of the following: slide backgrounds, title slide, fonts, pictures used in the slides, layout, charts, graphics, comparison versus, etc. If you have any ideas for the slide contents, please also provide any suggestions/recommendations.

I've also attached our vxMender logo if that is needed, as well as our brochure.

We look forward to your submissions!

EDIT:
I would like to add that we are using PowerPoint 2010 on a PC (.pptx file), and that the slides should be in 16:9 mainly but also with 4:3 version (if possible cut off the sides and squish in the content a little, no need to make a new set of slides) as sometimes we cannot control whose projector we are presenting on. Thanks

Target Market(s)

Enterprise clients, multi-national corporations,
banks, airlines, telecommunications, government

Industry/Entity Type

Software

Font styles to use
Serif
Sans Serif

Colors

Designer to choose colors to be used in the design.

Requirements
Nice to have
• Professional, clean-look, modern design
Should not have
• Should not look cheesy (i.e. tons of stock photos, business cliche pictures)
• Should not look over-done/over-the-top
• Should not look outdated

```html
<!DOCTYPE html>
<html lang="en">
<head>
<meta charset="utf-8">
<title>vxMender – Enterprise Chatbot Platform</title>
<link href="https://fonts.googleapis.com/css2?family=Open+Sans:ital,wght@0,400;0,600;0,700;1,400;1,600;1,700&display=swap" rel="stylesheet">
<style>
:root{
  --page:#e8ebee;
  --slide:#fbfcfd;
  --blue:#2f86d8;
  --deep:#3c64b4;
  --cyan:#1aa7e6;
  --dark:#3a3d42;
  --yellow:#f5b800;
  --green:#22b14c;
  --lime:#8dc63f;
  --orange:#f07d1e;
  --text:#4d5258;
  --muted:#9aa0a6;
  --rule:#d8dce0;
}
*{box-sizing:border-box;margin:0;padding:0}
html,body{width:1200px;height:688px;overflow:hidden}
body{background:var(--page);font-family:"Open Sans",Arial,sans-serif;color:var(--text);position:relative}
.slide{position:absolute;width:394px;height:224px;background:var(--slide);overflow:hidden;box-shadow:0 1px 3px rgba(0,0,0,.12)}
.abs{position:absolute}
.header-mark{position:absolute;left:0;top:15px;width:30px;height:10px;background:var(--blue);clip-path:polygon(0 0,60% 0,48% 100%,0 100%)}
.header-mark::after{content:"";position:absolute;left:0;top:0;width:100%;height:100%;background:var(--cyan);clip-path:polygon(70% 0,92% 0,80% 100%,58% 100%)}
.slide-title{position:absolute;left:30px;top:14px;font-size:8px;font-style:italic;color:var(--dark)}
.slide-title b{font-weight:700}
.logo{position:absolute;right:10px;top:13px;display:flex;align-items:center;gap:3px;font-size:9px;font-weight:600;color:var(--blue)}
.logo-dot{width:9px;height:9px;border-radius:50%;background:var(--blue)}
.footer{position:absolute;left:0;bottom:0;width:100%;height:6px;background:var(--dark)}
.footer::after{content:"";position:absolute;right:0;bottom:0;width:22px;height:14px;background:var(--cyan);clip-path:polygon(45% 0,100% 0,100% 100%,0 100%)}
.footer-links{position:absolute;left:0;right:0;bottom:1px;text-align:center;font-size:3px;color:#aeb3b8;letter-spacing:.2px}
.page-no{position:absolute;right:24px;bottom:8px;font-size:4px;color:var(--muted)}
.lead{position:absolute;left:0;right:0;text-align:center;font-size:6.4px;color:var(--text)}
.tiny{font-size:3.4px;line-height:1.4;color:var(--muted)}
.placeholder{position:absolute}

/* title */
.hero-art{position:absolute;left:120px;top:0;width:274px;height:224px;background:radial-gradient(ellipse at 70% 60%,#9fd0f3 0%,#cfe7f8 35%,rgba(251,252,253,0) 70%),linear-gradient(160deg,#eaf5fd 0%,#bfe0f7 55%,#6fb7ea 100%);clip-path:polygon(30% 0,100% 0,100% 100%,0 100%,22% 60%)}
.hero-kicker{position:absolute;left:16px;top:131px;font-size:11px;color:var(--cyan);letter-spacing:.3px}
.hero-title{position:absolute;left:16px;top:144px;font-size:11px;font-weight:700;color:var(--cyan);letter-spacing:.3px}
.hero-by{position:absolute;left:16px;top:161px;font-size:9.5px;color:var(--dark)}
.hero-date{position:absolute;left:16px;top:175px;font-size:7.5px;font-weight:700;color:var(--dark)}
.url-pill{position:absolute;left:14px;top:190px;width:119px;height:14px;border:1px solid var(--blue);border-radius:8px;background:#fff;font-size:5.5px;line-height:12px;padding-left:34px;color:var(--dark)}
.url-pill::before{content:"";position:absolute;left:-1px;top:-1px;width:22px;height:14px;border-radius:8px 0 0 8px;background:var(--blue)}
.url-pill::after{content:"";position:absolute;left:6px;top:3px;width:6px;height:6px;border:1px solid #fff;border-radius:50%}
.title-logo{left:15px;top:12px;right:auto;font-size:11px}
.title-logo .logo-dot{width:11px;height:11px}

/* agenda */
.agenda-item{position:absolute;width:80px}
.agenda-tab{position:relative;width:38px;height:8px;background:var(--dark);clip-path:polygon(0 0,100% 0,88% 100%,0 100%);font-size:3.6px;color:#fff;line-height:8px;padding-left:4px}
.agenda-tab::after{content:"";position:absolute;left:23px;top:0;width:14px;height:8px;background:var(--cyan);clip-path:polygon(40% 0,100% 0,60% 100%,0 100%)}
.agenda-sub{font-size:4.8px;color:var(--dark);margin-top:8px}
.agenda-item .tiny{margin-top:4px}

/* context columns */
.col-head{position:absolute;top:74px;width:97px;height:13px;font-size:3.4px;font-weight:700;color:#fff;text-align:center;line-height:1.3;padding-top:2px;text-transform:uppercase}
.col-sep{position:absolute;top:74px;width:1px;height:110px;background:var(--rule)}
.partner{position:absolute;font-weight:700;color:var(--deep)}
.banner{position:absolute;height:13px;display:flex}
.banner-play{width:115px;background:var(--deep);position:relative}
.banner-play::after{content:"";position:absolute;left:54px;top:4px;border-left:4px solid #fff;border-top:2.5px solid transparent;border-bottom:2.5px solid transparent}
.banner-text{flex:1;background:var(--cyan);color:#fff;font-size:3.6px;font-weight:600;text-align:center;line-height:13px}

/* chart slide */
.quote{position:absolute;left:60px;right:60px;top:41px;text-align:center;font-size:6.6px;font-style:italic;color:var(--text);line-height:1.4}
.quote-rule{position:absolute;left:50px;width:296px;top:67px;height:1px;background:var(--deep)}
.legend{position:absolute;left:270px;top:104px;font-size:6.6px;color:var(--text)}
.legend div{display:flex;align-items:flex-start;gap:3px;margin-bottom:7px;line-height:1.2}
.legend i{display:inline-block;width:9px;height:2px;margin-top:3px}

/* cards */
.card{position:absolute;top:66px;width:92px;height:115px;background:#fff;border:1px solid #e1e4e7}
.card-photo{position:absolute;left:3px;top:3px;width:84px;height:60px}
.card-num{position:absolute;left:3px;top:3px;width:15px;height:12px;background:var(--orange);color:#fff;font-size:6px;line-height:12px;text-align:center}
.card-title{position:absolute;left:6px;top:70px;font-size:9.5px;font-weight:600}
.card .tiny{position:absolute;left:6px;right:5px;top:85px;color:var(--text);font-size:3.3px}

/* intro */
.step-line{position:absolute;left:30px;top:66px;width:320px;height:1px;background:var(--rule)}
.step-start{position:absolute;left:26px;top:64px;width:5px;height:5px;border-radius:50%;background:var(--muted)}
.step-end{position:absolute;left:350px;top:63.5px;border-left:5px solid var(--muted);border-top:3px solid transparent;border-bottom:3px solid transparent}
.step-icon{position:absolute;top:55px;width:22px;height:22px;border-radius:50%;background:#fff;border:1px solid var(--rule);display:flex;align-items:center;justify-content:center}
.step-icon span{width:12px;height:12px;border-radius:50%}
.step-label{position:absolute;top:93px;width:54.6px;height:13px;font-size:3.4px;font-weight:600;color:#fff;text-align:center;line-height:1.25;padding-top:1.5px}
.step-text{position:absolute;top:120px;width:46px;font-size:3.4px;line-height:1.45;color:var(--muted)}

/* comparison */
.cmp-head{position:absolute;left:22px;top:66px;display:flex;align-items:center;gap:5px;font-size:8px;font-weight:600;color:var(--dark)}
.gear{width:11px;height:11px;border-radius:50%;border:3px dotted var(--deep)}
.cmp-list{position:absolute;left:22px;top:92px;list-style:none;font-size:5.6px;color:var(--text)}
.cmp-list li{margin-bottom:6px;padding-left:9px;position:relative}
.cmp-list li::before{content:"";position:absolute;left:0;top:2px;width:3px;height:3px;border:1px solid var(--muted);border-radius:50%}
.cmp-divider{position:absolute;left:178px;top:58px;width:0;height:120px;border-left:1px dashed var(--rule)}
.cmp-logo{position:absolute;left:210px;top:62px;display:flex;align-items:center;gap:4px;font-size:12px;color:var(--blue)}
.cmp-logo .logo-dot{width:14px;height:14px}
.win{position:absolute;left:212px;font-size:7.4px;font-weight:600;color:var(--blue);padding-left:9px}
.win::before{content:"";position:absolute;left:0;top:3px;border-left:3px solid var(--blue);border-top:2px solid transparent;border-bottom:2px solid transparent}
.win-sub{position:absolute;left:234px;font-size:5.2px;color:var(--muted);padding-left:8px}
.win-sub::before{content:"";position:absolute;left:0;top:2px;width:3px;height:3px;border:1px solid var(--muted);border-radius:50%}

/* speed chart */
.tier{position:absolute;left:42px;font-size:5.6px;color:var(--text);display:flex;align-items:center;gap:8px}
.tier i{width:9px;height:9px;border-radius:50%;background:#d6d9dc}
.axis-label{position:absolute;left:230px;top:187px;font-size:5.6px;color:var(--text)}

/* implementation */
.chev{position:absolute;top:93px;width:70px;height:14px;color:#fff;font-size:4.8px;font-weight:600;text-align:center;line-height:14px;clip-path:polygon(0 0,88% 0,100% 50%,88% 100%,0 100%,10% 50%)}
.chev-first{clip-path:polygon(0 0,88% 0,100% 50%,88% 100%,0 100%)}
.chev-text{position:absolute;top:112px;width:60px;font-size:4px;line-height:1.35;color:var(--text)}
.chev-sep{position:absolute;top:108px;width:1px;height:24px;background:var(--rule)}
</style>
</head>
<body>

<section class="slide" style="left:4px;top:6px">
  <div class="hero-art" role="img" aria-label="Abstract blue light streaks and translucent squares flowing to the right"></div>
  <div class="logo title-logo"><span class="logo-dot"></span>vxMender</div>
  <div class="hero-kicker">ENTERPRISE</div>
  <div class="hero-title">CHATBOT PLATFORM</div>
  <div class="hero-by">Presented by: Jordan Vale</div>
  <div class="hero-date">April 2017</div>
  <div class="url-pill">www.vxmender.com</div>
</section>

<section class="slide" style="left:404px;top:6px">
  <div class="header-mark"></div>
  <div class="slide-title">Presentation <b>AGENDA</b></div>
  <div class="logo"><span class="logo-dot"></span>vxMender</div>
  <div class="agenda-item" style="left:26px;top:56px"><div class="agenda-tab">01</div><div class="agenda-sub">Subtitle Goes Here</div><div class="tiny">Lorem ipsum dolor sit amet,<br>consectetur adipiscing elit.</div></div>
  <div class="agenda-item" style="left:114px;top:56px"><div class="agenda-tab">02</div><div class="agenda-sub">Subtitle Goes Here</div><div class="tiny">Lorem ipsum dolor sit amet,<br>consectetur adipiscing elit.</div></div>
  <div class="agenda-item" style="left:202px;top:56px"><div class="agenda-tab">03</div><div class="agenda-sub">Subtitle Goes Here</div><div class="tiny">Lorem ipsum dolor sit amet,<br>consectetur adipiscing elit.</div></div>
  <div class="agenda-item" style="left:290px;top:56px"><div class="agenda-tab">04</div><div class="agenda-sub">Subtitle Goes Here</div><div class="tiny">Lorem ipsum dolor sit amet,<br>consectetur adipiscing elit.</div></div>
  <div class="agenda-item" style="left:26px;top:123px"><div class="agenda-tab">05</div><div class="agenda-sub">Subtitle Goes Here</div><div class="tiny">Lorem ipsum dolor sit amet,<br>consectetur adipiscing elit.</div></div>
  <div class="agenda-item" style="left:114px;top:123px"><div class="agenda-tab">06</div><div class="agenda-sub">Subtitle Goes Here</div><div class="tiny">Lorem ipsum dolor sit amet,<br>consectetur adipiscing elit.</div></div>
  <div class="agenda-item" style="left:202px;top:123px"><div class="agenda-tab">07</div><div class="agenda-sub">Subtitle Goes Here</div><div class="tiny">Lorem ipsum dolor sit amet,<br>consectetur adipiscing elit.</div></div>
  <div class="agenda-item" style="left:290px;top:123px"><div class="agenda-tab">08</div><div class="agenda-sub">Subtitle Goes Here</div><div class="tiny">Lorem ipsum dolor sit amet,<br>consectetur adipiscing elit.</div></div>
  <div class="page-no">2</div>
  <div class="footer"></div>
  <div class="footer-links">vxmender.com · @vxmender · /vxmender · info@vxmender.com</div>
</section>

<section class="slide" style="left:803px;top:6px">
  <div class="header-mark"></div>
  <div class="slide-title"><b>CONTEXT</b></div>
  <div class="logo"><span class="logo-dot"></span>vxMender</div>
  <div class="lead" style="top:49px">We've spent the last ~25 years building end-to-end automation solutions for leading companies</div>
  <div class="col-head" style="left:26px;background:var(--yellow)">A track record of long term<br>relationships with top companies</div>
  <div class="col-head" style="left:141px;background:var(--cyan)">Experts in custom automation +<br>business intelligence systems</div>
  <div class="col-head" style="left:255px;background:var(--deep)">Toronto – based, but with a growing<br>global footprint</div>
  <div class="col-sep" style="left:131px"></div>
  <div class="col-sep" style="left:246px"></div>
  <div class="partner" style="left:28px;top:104px;font-size:9px">Northline</div>
  <div class="partner" style="left:78px;top:108px;font-size:5.5px">Paycrest</div>
  <div class="partner" style="left:52px;top:139px;font-size:7px">AutoGuild</div>
  <div class="placeholder" role="img" aria-label="Illustration of a network brain in blue" style="left:166px;top:98px;width:56px;height:50px;border-radius:45%;background:radial-gradient(circle,#5ab8ee,#1c93da)"></div>
  <div class="placeholder" role="img" aria-label="World map highlighting global presence in blue" style="left:262px;top:104px;width:86px;height:40px;border-radius:20px;background:linear-gradient(90deg,#9ea3a8 0%,#9ea3a8 45%,#3c64b4 55%,#3c64b4 100%);opacity:.85"></div>
  <div class="banner" style="left:26px;top:184px;width:336px"><div class="banner-play"></div><div class="banner-text">25 years including Velara and its predecessor, Orbitel Solutions</div></div>
  <div class="page-no">3</div>
  <div class="footer"></div>
  <div class="footer-links">vxmender.com · @vxmender · /vxmender · info@vxmender.com</div>
</section>

<section class="slide" style="left:4px;top:234px">
  <div class="header-mark"></div>
  <div class="slide-title"><b>CONTEXT</b></div>
  <div class="logo"><span class="logo-dot"></span>vxMender</div>
  <div class="quote">And because of technology, the way these companies interact with their customers is about to change!</div>
  <div class="quote-rule"></div>
  <svg class="abs" style="left:56px;top:72px" width="210" height="140" viewBox="0 0 210 140" font-family="Open Sans, sans-serif">
    <g stroke="#e3e6e9" stroke-width=".6">
      <line x1="20" y1="20" x2="200" y2="20"/><line x1="20" y1="40" x2="200" y2="40"/><line x1="20" y1="60" x2="200" y2="60"/><line x1="20" y1="80" x2="200" y2="80"/><line x1="20" y1="100" x2="200" y2="100"/>
    </g>
    <line x1="20" y1="10" x2="20" y2="120" stroke="#b8bcc0" stroke-width=".8"/>
    <line x1="20" y1="120" x2="200" y2="120" stroke="#b8bcc0" stroke-width=".8"/>
    <path d="M32 119 C110 115 150 95 177 46" fill="none" stroke="#f5b800" stroke-width="2"/>
    <path d="M32 118 C110 112 150 85 176 34" fill="none" stroke="#3c64b4" stroke-width="2"/>
    <path d="M32 117 C110 110 152 78 176 24" fill="none" stroke="#2f86d8" stroke-width="2"/>
    <polygon points="176,20 173,28 179,27" fill="#2f86d8"/>
    <polygon points="176,30 173,38 179,37" fill="#3c64b4"/>
    <polygon points="177,42 174,50 180,49" fill="#f5b800"/>
    <g font-size="5.4" fill="#4d5258" text-anchor="middle">
      <text x="32" y="129">80s</text><text x="68" y="129">90s</text><text x="104" y="129">00s</text><text x="140" y="129">10s</text><text x="176" y="129">20s</text>
      <text x="104" y="138" font-size="6.6">Year</text>
    </g>
    <text x="9" y="78" font-size="5.8" fill="#4d5258" transform="rotate(-90 9 78)">Maturity</text>
  </svg>
  <div class="legend">
    <div><i style="background:var(--blue)"></i>Artificial Intelligence</div>
    <div><i style="background:var(--deep)"></i>Machine Learning</div>
    <div><i style="background:var(--yellow)"></i>Natural Language<br>Processing</div>
  </div>
  <div class="page-no">4</div>
  <div class="footer"></div>
  <div class="footer-links">vxmender.com · @vxmender · /vxmender · info@vxmender.com</div>
</section>

<section class="slide" style="left:404px;top:234px">
  <div class="header-mark"></div>
  <div class="slide-title"><b>CONTEXT</b></div>
  <div class="logo"><span class="logo-dot"></span>vxMender</div>
  <div class="lead" style="top:41px">Digital customer experience is becoming the new battleground (for winning customer hearts and wallets)</div>
  <div class="card" style="left:27px">
    <div class="card-photo" role="img" aria-label="Photo of a smartphone showing a payment screen" style="background:linear-gradient(160deg,#5e6b72,#2f383d 60%,#7a8a6e)"></div>
    <div class="card-num">01</div>
    <div class="card-title" style="color:var(--lime)">On-demand</div>
    <div class="tiny">The quick, brown fox jumps over a lazy dog. Five boxing wizards jump quickly. Pack my box with five dozen jugs.</div>
  </div>
  <div class="card" style="left:147px">
    <div class="card-photo" role="img" aria-label="Photo of hands holding a phone beside a coffee cup" style="background:linear-gradient(160deg,#cfc8bf,#8f8780 50%,#4a4440)"></div>
    <div class="card-num" style="background:var(--blue)">02</div>
    <div class="card-title" style="color:var(--orange)">Low Friction</div>
    <div class="tiny">The quick, brown fox jumps over a lazy dog. Five boxing wizards jump quickly. Pack my box with five dozen jugs.</div>
  </div>
  <div class="card" style="left:267px">
    <div class="card-photo" role="img" aria-label="Photo of a child using a tablet" style="background:linear-gradient(160deg,#e7b472,#b9743a 50%,#5a3a22)"></div>
    <div class="card-num">03</div>
    <div class="card-title" style="color:var(--orange)">Intuitive</div>
    <div class="tiny">The quick, brown fox jumps over a lazy dog. Five boxing wizards jump quickly. Pack my box with five dozen jugs.</div>
  </div>
  <div class="page-no">5</div>
  <div class="footer"></div>
  <div class="footer-links">vxmender.com · @vxmender · /vxmender · info@vxmender.com</div>
</section>

<section class="slide" style="left:803px;top:234px">
  <div class="header-mark"></div>
  <div class="slide-title">Introducing <b>VXMENDER</b></div>
  <div class="logo"><span class="logo-dot"></span>vxMender</div>
  <div class="step-line"></div><div class="step-start"></div><div class="step-end"></div>
  <div class="step-icon" style="left:40px"><span style="background:var(--deep)"></span></div>
  <div class="step-icon" style="left:95px"><span style="background:var(--cyan)"></span></div>
  <div class="step-icon" style="left:150px"><span style="background:var(--green)"></span></div>
  <div class="step-icon" style="left:204px"><span style="background:var(--lime)"></span></div>
  <div class="step-icon" style="left:259px"><span style="background:var(--yellow)"></span></div>
  <div class="step-icon" style="left:313px"><span style="background:var(--orange)"></span></div>
  <div class="step-label" style="left:24px;background:var(--deep)">Omni-Language<br>Performance</div>
  <div class="step-label" style="left:78.6px;background:var(--cyan)">Real World Natural<br>Language Interaction</div>
  <div class="step-label" style="left:133.2px;background:var(--green)">Mixed-Media Responses</div>
  <div class="step-label" style="left:187.8px;background:var(--lime)">Fast Impact</div>
  <div class="step-label" style="left:242.4px;background:var(--yellow)">Keeps your data secure</div>
  <div class="step-label" style="left:297px;background:var(--orange)">Low Cost Independent<br>Operations</div>
  <div class="step-text" style="left:31px">Quisque libero purus, bibendum nec quam sit amet, porta interdum ex.</div>
  <div class="step-text" style="left:85px">Quisque libero purus, bibendum nec quam sit amet, porta interdum ex.</div>
  <div class="step-text" style="left:140px">Quisque libero purus, bibendum nec quam sit amet, porta interdum ex.</div>
  <div class="step-text" style="left:194px">Quisque libero purus, bibendum nec quam sit amet, porta interdum ex.</div>
  <div class="step-text" style="left:249px">Quisque libero purus, bibendum nec quam sit amet, porta interdum ex.</div>
  <div class="step-text" style="left:304px">Quisque libero purus, bibendum nec quam sit amet, porta interdum ex.</div>
  <div class="banner" style="left:24px;top:158px;width:328px"><div class="banner-play" style="width:55px"></div><div class="banner-text">And it has a unique set of benefits for operators</div></div>
  <div class="page-no">6</div>
  <div class="footer"></div>
  <div class="footer-links">vxmender.com · @vxmender · /vxmender · info@vxmender.com</div>
</section>

<section class="slide" style="left:4px;top:461px">
  <div class="header-mark"></div>
  <div class="slide-title">Omni-Language <b>Performance</b></div>
  <div class="logo"><span class="logo-dot"></span>vxMender</div>
  <div class="cmp-head"><span class="gear"></span>Traditional AI/NLP</div>
  <ul class="cmp-list">
    <li>Language dependent: only 1 language at a time</li>
    <li>Rule-based</li>
    <li>Multiple layers of translation</li>
  </ul>
  <div class="cmp-divider"></div>
  <div class="cmp-logo"><span class="logo-dot"></span>vxMender</div>
  <div class="win" style="top:92px">Language independent</div>
  <div class="win-sub" style="top:106px">Supports all known written/spoken languages</div>
  <div class="win-sub" style="top:118px">Supports mixed-language dialogs</div>
  <div class="win" style="top:131px">Statistics-based</div>
  <div class="win-sub" style="top:145px">No translation layers</div>
  <div class="page-no">7</div>
  <div class="footer"></div>
  <div class="footer-links">vxmender.com · @vxmender · /vxmender · info@vxmender.com</div>
</section>

<section class="slide" style="left:404px;top:461px">
  <div class="header-mark"></div>
  <div class="slide-title">Accelerated <b>Speed to Impact</b></div>
  <div class="logo"><span class="logo-dot"></span>vxMender</div>
  <div class="tier" style="top:68px"><i></i>Niche Requests</div>
  <div class="tier" style="top:108px"><i></i>Frequent Requests</div>
  <div class="tier" style="top:155px"><i></i>Low-hanging fruit</div>
  <svg class="abs" style="left:0;top:0" width="394" height="224" viewBox="0 0 394 224">
    <g stroke="#f0b27a" stroke-width=".7" stroke-dasharray="2 2">
      <line x1="38" y1="87" x2="340" y2="87"/><line x1="38" y1="133" x2="340" y2="133"/>
    </g>
    <line x1="128" y1="68" x2="128" y2="181" stroke="#2b2e33" stroke-width=".9"/>
    <polygon points="128,64 126,69 130,69" fill="#2b2e33"/>
    <line x1="128" y1="181" x2="346" y2="181" stroke="#2b2e33" stroke-width=".9"/>
    <polygon points="350,181 345,179 345,183" fill="#2b2e33"/>
    <g fill="#2f86d8">
      <circle cx="139" cy="164" r="5.3"/><circle cx="162" cy="164" r="5.3"/><circle cx="185" cy="164" r="5.3"/><circle cx="207" cy="164" r="5.3"/><circle cx="230" cy="164" r="5.3"/><circle cx="253" cy="164" r="5.3"/><circle cx="276" cy="164" r="5.3"/><circle cx="298" cy="164" r="5.3"/><circle cx="321" cy="164" r="5.3"/>
      <circle cx="162" cy="141" r="5.3"/><circle cx="185" cy="141" r="5.3"/><circle cx="207" cy="141" r="5.3"/><circle cx="230" cy="141" r="5.3"/><circle cx="253" cy="141" r="5.3"/><circle cx="276" cy="141" r="5.3"/><circle cx="298" cy="141" r="5.3"/><circle cx="321" cy="141" r="5.3"/>
      <circle cx="162" cy="118" r="5.3"/><circle cx="185" cy="118" r="5.3"/><circle cx="207" cy="118" r="5.3"/><circle cx="230" cy="118" r="5.3"/><circle cx="253" cy="118" r="5.3"/><circle cx="276" cy="118" r="5.3"/><circle cx="298" cy="118" r="5.3"/><circle cx="321" cy="118" r="5.3"/>
      <circle cx="207" cy="95" r="5.3"/><circle cx="230" cy="95" r="5.3"/><circle cx="253" cy="95" r="5.3"/><circle cx="276" cy="95" r="5.3"/><circle cx="298" cy="95" r="5.3"/><circle cx="321" cy="95" r="5.3"/>
    </g>
    <g fill="#f5b800">
      <circle cx="253" cy="72" r="5.3"/><circle cx="276" cy="72" r="5.3"/><circle cx="298" cy="72" r="5.3"/><circle cx="321" cy="72" r="5.3"/>
    </g>
  </svg>
  <div class="axis-label">Time</div>
  <div class="page-no">8</div>
  <div class="footer"></div>
  <div class="footer-links">vxmender.com · @vxmender · /vxmender · info@vxmender.com</div>
</section>

<section class="slide" style="left:803px;top:461px">
  <div class="header-mark"></div>
  <div class="slide-title">Implementing <b>vxMender</b></div>
  <div class="logo"><span class="logo-dot"></span>vxMender</div>
  <div class="chev chev-first" style="left:26px;background:var(--deep)">1-2 weeks</div>
  <div class="chev" style="left:93px;background:var(--cyan)">2-8 weeks</div>
  <div class="chev" style="left:160px;background:var(--green)">2-4 weeks</div>
  <div class="chev" style="left:227px;background:var(--lime)">OnGoing</div>
  <div class="chev" style="left:294px;background:var(--yellow)">OnGoing</div>
  <div class="chev-text" style="left:30px">Gather existing training materials</div>
  <div class="chev-sep" style="left:92px"></div>
  <div class="chev-text" style="left:97px">Develop dialog flow together</div>
  <div class="chev-sep" style="left:159px"></div>
  <div class="chev-text" style="left:164px">Deploy vxMender on your platform</div>
  <div class="chev-sep" style="left:226px"></div>
  <div class="chev-text" style="left:231px">Semi-automatic mode: Trained on-the-job and continually improves</div>
  <div class="chev-sep" style="left:293px"></div>
  <div class="chev-text" style="left:298px">Automatic mode: Handles visitors on its own</div>
  <div class="page-no">9</div>
  <div class="footer"></div>
  <div class="footer-links">vxmender.com · @vxmender · /vxmender · info@vxmender.com</div>
</section>

</body>
</html>
```